Digital Billboard Design: Winter Sales Event

I own a boutique furniture store in Calgary, AB (maplecrestdecor.ca) and I am looking to advertise our winter sale event on a new curved digital billboard (specs attached including required file type).

I have this billboard rented for 52-weeks so I will be looking to change the design every 4-weeks (i.e. this is intended to be an ongoing project).

The objective of this first billboard is to raise awareness around our annual winter sales event. The store itself is only a few blocks from the billboard so those commuting into downtown are just a short drive from the store.

I am looking for a fresh, clean, contemporary look that will grab your attention as you drive into downtown Calgary without presenting to much info so as to be distracting (and overwhelming -- the billboard does not need to contain all info on my current marketing material). I should also note that the store caters to a higher-end, more sophisticated clientele so the graphics need to reflect the brand (i.e. we are not Brennick Furniture or Couch Depot!).

I have attached three files:

Billboard specs
Current marketing material advertising sale (and all relevant data)
An idea that is from an American furniture store that I think is interesting

Target Market(s)

Upper middle class, sophisticated client who appreciates the finer things in life.

Industry/Entity Type

Furniture Store

Font styles to use
Sans Serif

Requirements
Must have
• Company Logo
• Winter Sales Event - 20 to 60% off
• Address: 2743 8th Ave SW
Nice to have
• Image of furniture -- see our website www.maplecrestdecor.ca -- any photo from this site can be used
Should not have
• Too much text or visual distration

```html
<!DOCTYPE html>
<html lang="en">
<head>
<meta charset="utf-8">
<title>Maplecrest Decor – Winter Sales Event Billboard</title>
<link href="https://fonts.googleapis.com/css2?family=Montserrat:wght@300;400;600;700&display=swap" rel="stylesheet">
<style>
  :root {
    --page: #ffffff;
    --board: #ffffff;
    --ink: #222426;
    --grey-text: #77797c;
    --orange: #f96a00;
    --blue: #58c0e8;
    --blue-soft: #a9def2;
    --amber: #fcb316;
    --amber-soft: #fdd98a;
    --green: #45b95f;
    --green-soft: #a2dcae;
    --tile-blue: #d8e1ea;
    --tile-cream: #eeeee0;
    --tile-mauve: #c0b9c4;
    --tile-stone: #c9cac2;
    --tile-mist: #e7ebe8;
    --tile-blush: #efe4e2;
    --tile-rose: #e8dcdc;
    --fold: #a9aaae;
  }
  * { box-sizing: border-box; margin: 0; padding: 0; }
  html, body {
    width: 1200px; height: 1000px; overflow: hidden;
    background: var(--page);
    font-family: "Montserrat", sans-serif;
  }
  .billboard {
    position: absolute; left: 62px; top: 249px;
    width: 828px; height: 386px;
    transform: scale(1.3); transform-origin: top left;
    background: var(--board);
    overflow: hidden;
  }
  .brand {
    position: absolute; left: 28px; top: 34px;
    font-size: 13px; font-weight: 400; letter-spacing: 1.6px;
    color: var(--ink); text-transform: uppercase;
  }
  .event-ribbons { position: absolute; left: 0; top: 100px; width: 290px; height: 145px; }
  .ribbon-label {
    position: absolute; left: 30px; height: 36px; line-height: 37px;
    font-size: 25px; color: #fff; letter-spacing: 0.5px; text-transform: uppercase;
  }
  .ribbon-label.winter { top: 107px; font-weight: 300; }
  .ribbon-label.sales { top: 153px; font-weight: 700; }
  .ribbon-label.event { top: 199px; font-weight: 300; }
  .contact {
    position: absolute; left: 28px; top: 293px;
    font-size: 14px; line-height: 18.5px; color: var(--grey-text);
    text-transform: uppercase; letter-spacing: 0.3px;
  }
  .contact .web { font-weight: 600; }
  .offer-column {
    position: absolute; left: 282px; top: 0; width: 177px; height: 386px;
    background: var(--orange);
  }
  .offer-notch {
    position: absolute; left: -30px; top: 143px;
    width: 60px; height: 60px; border-radius: 50%; background: var(--board);
  }
  .discount {
    position: absolute; right: 20px; top: 198px;
    text-align: right; color: #fff; text-transform: uppercase;
  }
  .discount .figure { display: block; font-size: 52px; font-weight: 700; line-height: 46px; }
  .discount .word { display: block; font-size: 29px; font-weight: 300; line-height: 28px; letter-spacing: 1px; }
  .product-grid {
    position: absolute; left: 483px; top: 36px;
    display: grid; grid-template-columns: repeat(4, 77px); grid-auto-rows: 77px;
    column-gap: 4px; row-gap: 3px;
  }
  .tile { position: relative; }
  .tile.fold-br::after, .tile.fold-tr::after, .tile.fold-bl::after, .tile.fold-tl::after {
    content: ""; position: absolute; width: 16px; height: 16px; background: var(--fold);
  }
  .tile.fold-br::after { right: 0; bottom: 0; clip-path: polygon(0 0, 100% 0, 0 100%); background: linear-gradient(135deg, var(--fold), #d6d7da); }
  .tile.fold-tr::after { right: 0; top: 0; clip-path: polygon(0 0, 0 100%, 100% 100%); }
  .tile.fold-bl::after { left: 0; bottom: 0; clip-path: polygon(0 0, 100% 0, 100% 100%); }
  .tile.fold-tl::after { left: 0; top: 0; clip-path: polygon(100% 0, 100% 100%, 0 100%); }
  .blue { background: var(--tile-blue); }
  .cream { background: var(--tile-cream); }
  .mauve { background: var(--tile-mauve); }
  .stone { background: var(--tile-stone); }
  .mist { background: var(--tile-mist); }
  .blush { background: var(--tile-blush); }
  .rose { background: var(--tile-rose); }
  .white { background: #ffffff; }
</style>
</head>
<body>
  <main class="billboard">
    <div class="brand">Maplecrest Decor</div>

    <svg class="event-ribbons" viewBox="0 100 290 145" aria-hidden="true">
      <polygon points="165,107 283,173 165,143" fill="var(--blue-soft)"/>
      <polygon points="165,153 283,173 165,189" fill="var(--amber-soft)"/>
      <polygon points="165,199 283,173 165,235" fill="var(--green-soft)"/>
      <rect x="0" y="107" width="165" height="36" fill="var(--blue)"/>
      <rect x="0" y="153" width="165" height="36" fill="var(--amber)"/>
      <rect x="0" y="199" width="165" height="36" fill="var(--green)"/>
    </svg>
    <div class="ribbon-label winter">Winter</div>
    <div class="ribbon-label sales">Sales</div>
    <div class="ribbon-label event">Event</div>

    <address class="contact" style="font-style:normal">
      403.555.0182<br>
      <span class="web">www.maplecrestdecor.ca</span><br>
      2743 8th Ave SW,<br>
      Calgary, AB
    </address>

    <section class="offer-column">
      <div class="offer-notch"></div>
      <div class="discount">
        <span class="figure">20</span>
        <span class="word">to</span>
        <span class="figure">60%</span>
        <span class="word">off</span>
      </div>
    </section>

    <section class="product-grid">
      <div class="tile blue fold-bl" role="img" aria-label="Dark wood round dining table"></div>
      <div class="tile cream"></div>
      <div class="tile white" role="img" aria-label="Glass-top coffee table on chrome base"></div>
      <div class="tile stone fold-br" role="img" aria-label="Black bar stool on chrome stand"></div>

      <div class="tile mauve"></div>
      <div class="tile blue fold-br" role="img" aria-label="Black tufted leather ottoman"></div>
      <div class="tile mist" role="img" aria-label="Chrome and glass side table"></div>
      <div class="tile blue fold-tl" role="img" aria-label="Grey upholstered lounge chair"></div>

      <div class="tile blue fold-br" role="img" aria-label="Dark round cocktail table"></div>
      <div class="tile white"></div>
      <div class="tile blue fold-tl" role="img" aria-label="Green glass table lamp"></div>
      <div class="tile blue fold-br" role="img" aria-label="Black geometric accent table"></div>

      <div class="tile blush" role="img" aria-label="Grey mid-century sofa"></div>
      <div class="tile blue fold-tl" role="img" aria-label="Black and white sideboard"></div>
      <div class="tile blue"></div>
      <div class="tile rose fold-tl" role="img" aria-label="Dark wood display cabinet"></div>
    </section>
  </main>
</body>
</html>
```